Morden, Creative, Unique, Independent Wine Shop

1. We are a brand new wine shop located in Melbourne Australia, we have our logo already, simply use the logo to design a business card.
2. I have uploaded our logo in two versions, with or without shadow, any of them is acceptable.
3. Make it as creative and unique as possible, no limitation of shape, color combination, geometry pattern, fonts, composing etc.
3. Info on the card:
- Brambleford Wine Cellar (Not very necessary if logo is obviously shown)
- 42 Ferncastle Steet, Larkvale, Westmoor, Australia 4821
- +61 3 9018 4637
- www.bramblefordwinecellar.com.au
- bramblefordwinecellar@mailvista.com
- Additional icons: Google, Instagram, Facebook, Twitter
4. Once again, forget it is a commercial card, make it special.

```html
<!DOCTYPE html>
<html lang="en">
<head>
<meta charset="utf-8">
<title>Brambleford Wine Cellar – Business Card</title>
<link href="https://fonts.googleapis.com/css2?family=Arimo:wght@400;700&display=swap" rel="stylesheet">
<style>
  :root {
    --backdrop: #d9d9da;
    --wine-bright: #a80b33;
    --wine-mid: #8a0420;
    --wine-deep: #5e000e;
    --ink-white: #ffffff;
    --rule: rgba(255,255,255,0.75);
    --mark-silver: #c9c9cc;
    --mark-dark: #2b070d;
  }
  * { box-sizing: border-box; margin: 0; padding: 0; }
  html, body { width: 1200px; height: 800px; overflow: hidden; }
  body {
    background: var(--backdrop);
    font-family: "Arimo", Arial, sans-serif;
    position: relative;
  }
  .card {
    position: absolute;
    left: 320px;
    width: 560px;
    height: 320px;
    border-radius: 22px;
    background: radial-gradient(ellipse at 45% 50%, var(--wine-bright) 0%, var(--wine-mid) 45%, var(--wine-deep) 100%);
    box-shadow: 0 8px 24px rgba(0,0,0,0.25);
    overflow: hidden;
  }
  .card--back { top: 60px; }
  .card--front { top: 420px; }

  /* Back side */
  .holder {
    position: absolute;
    right: 330px;
    top: 136px;
    text-align: right;
    color: var(--ink-white);
  }
  .holder__name {
    font-weight: 700;
    font-size: 21px;
    letter-spacing: 0.3px;
  }
  .holder__title {
    font-weight: 700;
    font-size: 13px;
    margin-top: 2px;
  }
  .divider {
    position: absolute;
    left: 250px;
    top: 96px;
    width: 1px;
    height: 128px;
    background: var(--rule);
  }
  .contact {
    position: absolute;
    left: 270px;
    top: 100px;
    color: var(--ink-white);
    font-size: 13px;
    line-height: 17px;
  }
  .contact__address { margin-bottom: 10px; }
  .contact__row {
    display: flex;
    align-items: center;
    gap: 7px;
  }
  .contact__row svg { width: 10px; height: 10px; flex: none; fill: var(--ink-white); }

  /* Front side */
  .brand {
    position: absolute;
    inset: 0;
    display: flex;
    align-items: center;
    justify-content: center;
    gap: 16px;
  }
  .brand__dot {
    width: 58px;
    height: 58px;
    border-radius: 50%;
    background: var(--mark-silver);
  }
  .brand__name {
    font-weight: 400;
    font-size: 34px;
    letter-spacing: 1px;
    color: var(--mark-dark);
  }
</style>
</head>
<body>
  <section class="card card--back" aria-label="Card back with contact details">
    <div class="holder">
      <p class="holder__name">DANIEL HARTLEY</p>
      <p class="holder__title">President</p>
    </div>
    <div class="divider"></div>
    <div class="contact">
      <p class="contact__address">42 Ferncastle Steet, Larkvale<br>Westmoor, Australia 4821</p>
      <p class="contact__row">
        <svg viewBox="0 0 10 10" aria-hidden="true"><path d="M2 0.5 L3.6 2.6 L2.7 3.6 C3.3 5 4.9 6.6 6.4 7.3 L7.4 6.4 L9.5 8 L8.3 9.5 C4.5 9 1 5.5 0.5 1.7 Z"/></svg>
        +61 3 9018 4637
      </p>
      <p class="contact__row">
        <svg viewBox="0 0 10 10" aria-hidden="true"><path d="M0 2 H10 V8.5 H0 Z M0.8 2.6 L5 5.6 L9.2 2.6" fill="var(--ink-white)" stroke="var(--wine-mid)" stroke-width="0.8"/></svg>
        bramblefordwinecellar@mailvista.com
      </p>
      <p class="contact__row">
        <svg viewBox="0 0 10 10" aria-hidden="true"><circle cx="5" cy="5" r="4.6"/><path d="M0.6 5 H9.4 M5 0.4 C2.6 3 2.6 7 5 9.6 M5 0.4 C7.4 3 7.4 7 5 9.6" fill="none" stroke="var(--wine-mid)" stroke-width="0.7"/></svg>
        www.bramblefordwinecellar.com.au
      </p>
    </div>
  </section>

  <section class="card card--front" aria-label="Card front with brand name">
    <div class="brand">
      <span class="brand__dot" aria-hidden="true"></span>
      <p class="brand__name">Brambleford Wine Cellar</p>
    </div>
  </section>
</body>
</html>
```